KMR Brochure

Brochure to communicate the concept and financial value of the company and its services to an executive audience. Attachments have detailed copy I want to use.
Updates

I have added a file that includes high res versions of company logo.

Reason: I am worried that the feedback and creation of new versions may take too long to complete by Sunday! This deadline will NOT move again though.

Target Market(s)

Chief Financial Officers in hospitals and other health organizations

Industry/Entity Type

Financial

Requirements
Must have
• Must be a 2-sided, single page.

```html
<!DOCTYPE html>
<html lang="en">
<head>
<meta charset="utf-8">
<title>KMR Brochure</title>
<link rel="stylesheet" href="https://fonts.googleapis.com/css2?family=Open+Sans:wght@300;400;600;700&display=swap">
<style>
  :root{
    --page:#e6e6e6;
    --paper:#ffffff;
    --green:#9ab446;
    --blue:#2e6fad;
    --dark:#2b2b2b;
    --ink:#222222;
    --muted:#444444;
  }
  *{box-sizing:border-box;margin:0;padding:0}
  html,body{width:780px;height:1200px;overflow:hidden;background:var(--page)}
  body{position:relative;font-family:"Open Sans",Arial,sans-serif;color:var(--ink)}
  .abs{position:absolute}
  .sheet{position:absolute;left:17px;width:746px;background:var(--paper)}
  .sheet--outside{top:17px;height:576px}
  .sheet--inside{top:605px;height:580px}

  /* outside */
  .about{left:18px;top:200px;width:222px;font-size:8.1px;line-height:1.2;text-align:justify;color:var(--ink)}
  .about h2{font-size:10.5px;font-weight:700;line-height:1.15;margin-bottom:11px;text-align:left}
  .about p{margin-bottom:9px}
  .band-green{background:var(--green)}
  .band-blue{background:var(--blue)}
  .band-dark{background:var(--dark)}
  .photo{background:linear-gradient(135deg,#f4efe9 0%,#e7c4a6 55%,#c98f6a 100%)}
  .photo--family{background:linear-gradient(170deg,#eef3f7 0%,#c7d8e2 35%,#b88a6c 65%,#6f9a3c 100%)}

  .brand{display:flex;align-items:center;gap:8px}
  .brand__mark{width:22px;height:22px;background:var(--green)}
  .brand__name{font-weight:600;letter-spacing:1px}
  .brand--small .brand__name{font-size:20px;color:var(--dark)}
  .brand--large .brand__mark{width:34px;height:34px}
  .brand--large .brand__name{font-size:34px;color:#ffffff;font-weight:400}

  .contact{font-size:10.5px;line-height:1.35;color:var(--ink)}
  .contact strong{font-weight:700}
  .tagline{color:#d8d8d8;font-weight:300;font-size:12.5px}

  /* inside grid */
  .cell{position:absolute;padding:13px}
  .card{background:var(--paper);width:100%;height:100%;position:relative}
  .card__art{position:absolute;left:8px;top:10px;width:96px;height:72px}
  .art-chart{background:linear-gradient(135deg,#f2f2f2,#c9d3de 60%,#7a93b5)}
  .art-building{background:linear-gradient(135deg,#e7d7c6,#c98d5c 55%,#7e6aa0)}
  .art-glasses{background:linear-gradient(135deg,#f4f4f4,#b8c6d8 55%,#3f6fae)}
  .card__title{position:absolute;left:108px;right:8px;top:10px;height:28px;background:var(--dark);color:#fff;font-size:10.5px;font-weight:600;line-height:1.1;padding:3px 8px;display:flex;align-items:center}
  .card__title--center{justify-content:center;font-size:11.5px}
  .card__lead{position:absolute;left:112px;right:8px;top:42px;font-size:7.9px;font-weight:700;line-height:1.2}
  .card__body{position:absolute;left:16px;right:12px;top:112px;font-size:8.2px;line-height:1.3;color:var(--muted)}
  .card__body b{color:var(--ink)}

  .footer-band{left:0;top:514px;width:746px;height:66px;background:linear-gradient(90deg,#262626,#3a3a3a 50%,#262626);display:flex;align-items:center;justify-content:center}
  .footer-band span{color:#e8e8e8;font-size:22px;font-weight:300}
</style>
</head>
<body>

<section class="sheet sheet--outside">
  <div class="about abs">
    <h2>About<br>KMR</h2>
    <p>Leaders are dealing with new complexity as the business of patient care evolves from a volume-driven model to one based largely on outcomes. The leader's challenge is to navigate this transformation, adapt the organization to it, while remaining focused on operational priorities, such as achieving cost reduction in an industry with a history and culture of high cost growth.</p>
    <p>KMR brings together innovative, results-oriented professional services firms to achieve substantial, quantifiable breakthroughs in financial performance for healthcare organizations. We have assembled exceptional talent and diverse ideas from business, engineering, and applied mathematics to deliver performance improvement - cost savings and net revenue increases - to hospitals, nursing homes, large physician practices, surgery centers, and health insurers.</p>
    <p>Unlike large management consulting firms, which work primarily on a fixed retainer basis and focus on recommendations, our emphasis is on implementation and follow-through. This enables clients to pay only for the measured results we create, avoiding financial risk.</p>
    <p>Measurement methods are simple and mutually agreed upon in advance, with fees paid after results have been achieved and measured. Cash flow impact to the client is positive from day 1. Traditional fixed-fee or 'hybrid' arrangements are also options.</p>
  </div>

  <div class="abs band-green" style="left:249px;top:0;width:248px;height:277px"></div>
  <div class="brand brand--small abs" style="left:276px;top:427px">
    <span class="brand__mark"></span><span class="brand__name">KMR</span>
  </div>
  <div class="contact abs" style="left:276px;top:470px">
    4100 Harbor Way<br>Lakeview, WA 98000<br><strong>(555) 014-2290</strong><br>info@kmrpartners.example<br>www.kmrhealth.example
  </div>
  <div class="abs band-green" style="left:249px;top:554px;width:248px;height:22px"></div>

  <div class="abs photo" role="img" aria-label="Photo of two hands gently holding each other" style="left:497px;top:0;width:249px;height:277px"></div>
  <div class="abs band-green" style="left:497px;top:277px;width:249px;height:22px"></div>
  <div class="abs band-dark" style="left:497px;top:299px;width:249px;height:255px"></div>
  <div class="brand brand--large abs" style="left:533px;top:453px">
    <span class="brand__mark"></span><span class="brand__name">KMR</span>
  </div>
  <div class="tagline abs" style="left:523px;top:520px">Solutions for a stronger bottom line</div>
  <div class="abs band-blue" style="left:497px;top:554px;width:249px;height:22px"></div>
</section>

<section class="sheet sheet--inside">
  <div class="abs photo--family" role="img" aria-label="Photo of a smiling family of four lying stacked on a lawn" style="left:0;top:0;width:249px;height:361px"></div>
  <div class="brand brand--small abs" style="left:24px;top:385px">
    <span class="brand__mark"></span><span class="brand__name">KMR</span>
  </div>
  <div class="contact abs" style="left:24px;top:428px">
    4100 Harbor Way<br>Lakeview, WA 98000<br><strong>(555) 014-2290</strong><br>info@kmrpartners.example<br>www.kmrhealth.example
  </div>

  <div class="cell band-green" style="left:249px;top:0;width:249px;height:260px">
    <article class="card">
      <div class="card__art art-chart" role="img" aria-label="Illustration of a bar chart with a magnifying glass"></div>
      <h3 class="card__title">Strategic<br>Sourcing</h3>
      <p class="card__lead">Supplier spending often comprises 35-40% of a hospital's operating costs. This is a significant cost reduction opportunity.</p>
      <p class="card__body" style="top:118px">Using deep subject matter expertise and a large real time database, our sourcing efforts deliver an average savings of 18%. Our team has worked with over 500 clients since 1992, with experience in over 100 spend categories. We consistently exceed GPO savings.</p>
    </article>
  </div>

  <div class="cell band-blue" style="left:498px;top:0;width:248px;height:260px">
    <article class="card">
      <div class="card__art art-building" role="img" aria-label="Cutaway illustration of a building's energy systems"></div>
      <h3 class="card__title">Energy<br>Conservation</h3>
      <p class="card__lead">Hospitals are among the largest users of energy per sq ft. EPA estimates that an average of 30% of energy consumed by commercial buildings is wasted.</p>
      <p class="card__body" style="top:136px">Our engineers evaluate your facility's mechanical systems, controls, and energy usage, identifying and implementing non-capital projects that reduce consumption and costs by 10-30%.</p>
    </article>
  </div>

  <div class="cell band-blue" style="left:249px;top:260px;width:249px;height:254px">
    <article class="card">
      <div class="card__art art-glasses" role="img" aria-label="Photo of eyeglasses resting on a financial chart"></div>
      <h3 class="card__title">Surgical<br>Staffing</h3>
      <p class="card__lead">Facilities often provide surgical first assistance without reimbursement. Surgeons often ask colleagues to assist in cases.</p>
      <p class="card__body" style="top:126px">Our "in-sourcing" program provides trained professional surgical first assistants (SFA's) to hospitals and surgery centers to offset expenses, increase throughput, and provide the best possible support for surgeons and their patients.</p>
    </article>
  </div>

  <div class="cell band-green" style="left:498px;top:260px;width:248px;height:254px">
    <article class="card">
      <div class="card__art art-glasses" role="img" aria-label="Photo of eyeglasses resting on a financial chart"></div>
      <h3 class="card__title card__title--center">Revenue Analytics</h3>
      <p class="card__lead">Few hospitals realize the revenue-generating power of their data.</p>
      <p class="card__body" style="top:90px;left:14px;right:10px;font-size:7.9px;line-height:1.22"><b>Pricing.</b><br>Mathematically implemented strategic pricing, optimization of price sensitive net revenue based on market position, patient mix, contracts, and your business rules.<br><b>Charge Capture.</b><br>Analysis of charge data vs. a repository of standards. Analysis of completeness of claims to identify and realize revenue gains.<br><b>ICD-10.</b><br>Analytics to identify areas of high vs. low risk and complexity, enabling better prioritization of efforts.</p>
    </article>
  </div>

  <div class="footer-band abs"><span>Solutions for a stronger bottom line</span></div>
</section>

</body>
</html>
```